Legal Campaign

A courier compavny that offer Legal services like filing/recording Court documents.
Updates

These info must be on card: Can We Help With Your Legal Services? Need Your Court documents quickly filed? .Filing/Recording in Erie, Niagara & Monroe County .Pick-up within 15-30 minutes of call .Medical records pick-up & delivery .Court-Authorized Process Servers .$9.00 Buffalo to Buffalo .Volume Discounts Call Drew Halvorn@716-555-0143 The address must be 48 Tillman Ave., Buffalo NY 14209

Please add the following info: 1.Post Office Pickup/Deliveries 2. Drewhalvorn@qrtlane.com

Target Market(s)

Law firms & legal community.

Industry/Entity Type

Court

Requirements
Must have
• RoutaSwift logo must be on card. Please visit the website@qrtlane.com to check out the logo. Thanks

```html
<!DOCTYPE html>
<html lang="en">
<head>
<meta charset="utf-8">
<title>RoutaSwift Couriers – Legal Services Card</title>
<link rel="stylesheet" href="https://fonts.googleapis.com/css2?family=Open+Sans:wght@400;600;700;800&display=swap">
<style>
  :root {
    --white: #ffffff;
    --ink: #2b2b2b;
    --grey: #6f7072;
    --blue: #1f5ea8;
    --blue-deep: #0f57a6;
    --orange: #f7901e;
    --illus-light: #eceef1;
    --illus-mid: #d7dbe1;
  }
  * { margin: 0; padding: 0; box-sizing: border-box; }
  html, body { width: 1200px; height: 948px; overflow: hidden; background: var(--white); }
  body { font-family: "Open Sans", Arial, sans-serif; color: var(--ink); }

  .card { position: relative; width: 1200px; height: 948px; background: var(--white); overflow: hidden; }

  .brand { position: absolute; left: 52px; top: 48px; display: flex; align-items: center; gap: 18px; }
  .brand-mark { width: 30px; height: 30px; background: var(--grey); }
  .brand-name { font-weight: 800; font-size: 54px; line-height: 1.05; color: var(--grey); letter-spacing: 0.5px; }

  .headline { position: absolute; left: 540px; top: 66px; }
  .headline-ask { font-size: 33px; font-weight: 400; color: var(--ink); line-height: 1.2; }
  .headline-ask .accent { color: var(--orange); }
  .headline-need { margin-top: 16px; font-size: 29px; font-weight: 700; color: var(--ink); line-height: 1.2; }
  .headline-need .accent { color: var(--blue); }

  .rule { position: absolute; left: 0; top: 0; }

  .illustration {
    position: absolute; left: 40px; top: 320px; width: 420px; height: 420px;
    border-radius: 46% 54% 40% 60% / 50% 45% 55% 50%;
    background: radial-gradient(circle at 50% 45%, var(--illus-mid), var(--illus-light) 70%);
  }

  .offer { position: absolute; left: 540px; top: 352px; }
  .offer-title { font-size: 33px; font-weight: 700; color: var(--grey); text-decoration: underline; text-underline-offset: 6px; margin-bottom: 28px; }
  .offer-list { list-style: none; }
  .offer-list li { font-size: 23px; line-height: 1.25; height: 66px; color: var(--ink); white-space: nowrap; }
  .offer-list li::before { content: ">"; color: var(--blue); margin-right: 10px; }

  .badge { position: absolute; left: 960px; top: 620px; width: 210px; height: 210px; }
  .badge-text {
    position: absolute; left: 960px; top: 664px; width: 210px;
    text-align: center; color: var(--white); font-weight: 600; font-size: 21px; line-height: 1.45;
  }

  .footer-band { position: absolute; left: 0; top: 0; }
  .footer {
    position: absolute; left: 0; top: 884px; width: 1200px; height: 56px; padding: 0 44px;
    display: flex; align-items: center; justify-content: space-between;
    color: var(--white); font-weight: 600; font-size: 25px;
  }
  .footer-item { display: flex; align-items: center; gap: 10px; white-space: nowrap; }
  .footer-item svg { flex: none; }
</style>
</head>
<body>
<main class="card">

  <div class="brand">
    <div class="brand-mark"></div>
    <div class="brand-name">RoutaSwift<br>Couriers</div>
  </div>

  <header class="headline">
    <p class="headline-ask">Can We Help With Your <span class="accent">Legal Services</span>?</p>
    <p class="headline-need">Need Your Court <span class="accent">documents quickly filed</span>?</p>
  </header>

  <svg class="rule" width="1200" height="948" viewBox="0 0 1200 948" aria-hidden="true">
    <polyline points="0,258 458,258 500,222 1145,222 1200,182" fill="none" stroke="var(--blue)" stroke-width="3"/>
  </svg>

  <div class="illustration" role="img" aria-label="Illustration of an open binder with stacked file folders and papers"></div>

  <section class="offer">
    <h2 class="offer-title">WE OFFER</h2>
    <ul class="offer-list">
      <li>Filing/Recording in Erie, Niagara &amp; Monroe County</li>
      <li>Pick-up within 15-30 minutes of call</li>
      <li>Medical records pick-up &amp; delivery</li>
      <li>Court-Authorized Process Servers</li>
      <li>Post Office Pickup/Deliveries</li>
      <li>$9.00 Buffalo to Buffalo</li>
    </ul>
  </section>

  <svg class="badge" viewBox="0 0 220 220" aria-hidden="true">
    <circle cx="110" cy="110" r="106" fill="none" stroke="var(--grey)" stroke-width="3" stroke-dasharray="6 6"/>
    <path d="M110 14 C168 12 204 52 202 108 C200 160 176 196 128 202 C96 206 60 214 34 186 C10 160 16 118 22 82 C30 38 64 16 110 14 Z" fill="var(--blue-deep)"/>
  </svg>
  <div class="badge-text">Volume<br>Discounts<br>Call Drew<br>Halvorn</div>

  <svg class="footer-band" width="1200" height="948" viewBox="0 0 1200 948" aria-hidden="true">
    <polygon points="0,866 1118,866 1200,808 1200,948 0,948" fill="var(--orange)"/>
  </svg>

  <footer class="footer">
    <div class="footer-item">
      <svg width="20" height="27" viewBox="0 0 24 32" aria-hidden="true">
        <path d="M12 1C6 1 2 5.5 2 11c0 7.5 10 19 10 19s10-11.5 10-19C22 5.5 18 1 12 1Z" fill="none" stroke="var(--white)" stroke-width="3"/>
        <circle cx="12" cy="11" r="3.5" fill="none" stroke="var(--white)" stroke-width="3"/>
      </svg>
      <span>48 Tillman Ave., Buffalo NY 14209</span>
    </div>
    <div class="footer-item">
      <svg width="26" height="20" viewBox="0 0 26 20" aria-hidden="true">
        <rect x="1.5" y="1.5" width="23" height="17" rx="2" fill="none" stroke="var(--white)" stroke-width="2.5"/>
        <polyline points="2,3 13,11 24,3" fill="none" stroke="var(--white)" stroke-width="2.5"/>
      </svg>
      <span>Drewhalvorn@qrtlane.com</span>
    </div>
    <div class="footer-item">
      <svg width="22" height="22" viewBox="0 0 24 24" aria-hidden="true">
        <path d="M6.6 10.8c1.4 2.8 3.8 5.2 6.6 6.6l2.2-2.2c.3-.3.7-.4 1-.2 1.1.4 2.3.6 3.6.6.6 0 1 .4 1 1V20c0 .6-.4 1-1 1C10.6 21 3 13.4 3 4c0-.6.4-1 1-1h3.5c.6 0 1 .4 1 1 0 1.3.2 2.5.6 3.6.1.3 0 .7-.2 1l-2.3 2.2Z" fill="var(--white)"/>
      </svg>
      <span>716-555-0143</span>
    </div>
  </footer>

</main>
</body>
</html>
```